Web Design Project

Looking to create a skin (just need PSD files) for our very simple publishing retail website (it only comprises of 2-3 pages but it has to be beautiful).

Also looking to create a logo in the style of the Grintax.com logo but slightly differant (ie has to be clear that they are related but not the same) The basic website has been built : http://quorvelstudio.example/inprogress/mm/WebDev/

The general look and feel which we are after is: the new tandrell, the new hivenook page, zelpo.fm (basically very web 2.0)

Full Brief Below:

The basic point of it is that as a student you can tell us which university you are at and then which course/degree you are studying and then up pops a list of all of the recommended text books which you can buy from corrind.

A very similar site is but we are much simpler than them: www.pupilbookrosters.example We want it to be very minimalist and clean, like zelpo.fm

The colour scheme (though not the design) should also match the following website www.grintax.example You can ignore the input boxes on the bottom right and top right of the web page as they are not meant to be there.

The entire website only has three pages,: 1. Home Page, 2. Results page with Modules.3. Results Page with Books (when clicked on it should take you to Corrind).

Target Market(s)

University Students

Industry/Entity Type

University

Requirements
Must have
• Specific Requirements:

1. Top of the page should be the new logo (similar to Grintax but differant, also needs a new name: e.g. Grintax Books or Grintax Reading, Grintax Physical, Grintax Old School, Grintax Books

2. Top of the page should be a paragraph of text and an image telling them what the website is.

3. Below that there should be two search boxes in a row, which list: University and Course. These should be auto fill (we have all the data, as per the attached spread sheet so they should only be able to select from these). When they select from these then they should be taken to another page listing all of the books, which pertain to this course & university (as per the website)

4. There should also be a general search bar in the top right hand corner this where they can just search normally for any book in our database. This will then produce a list of books wich you can then buy on corrind

5. There should also be another area of text which relates to how we get the data and saying that we will give students free books if they email us their reading lists (if we don’t have them) and then they can email us to get a free book once we have checked that the data is correct. This should be an autofill box. Which they put their email into.

6. There should also be a box saying that students should sign up to Grintax.com (this should be on every page)

```html
<!DOCTYPE html>
<html lang="en">
<head>
<meta charset="utf-8">
<title>Grintax Books – Spectroscopy reading list</title>
<link rel="stylesheet" href="https://fonts.googleapis.com/css2?family=Open+Sans:wght@300;400;600&family=Oswald:wght@400;600&family=Caveat:wght@400;700&display=swap">
<style>
:root{
  --sky-top:#5bc3ee;
  --sky-bottom:#3aa8e0;
  --pink:#ec5a9e;
  --ink:#3d3d3d;
  --muted:#6a6a6a;
  --bar:#2a2a2a;
  --bar-btn:#333;
  --side:#2e2e2e;
  --side-line:#1c1c1c;
  --page:#efefef;
  --card:#fff;
  --strip:#dcdcdc;
  --footer:#1d1d1d;
  --banner:#3a3a3a;
  --banner-edge:#6f93ad;
}
*{box-sizing:border-box;margin:0;padding:0}
html,body{width:1200px;height:1200px;overflow:hidden}
body{position:relative;font-family:"Open Sans",Arial,sans-serif;background:var(--page);color:var(--ink)}
.abs{position:absolute}

/* header */
.site-header{position:absolute;left:0;top:0;width:1200px;height:130px;background:linear-gradient(var(--sky-top),var(--sky-bottom));border-bottom:1px solid #8fd6f5}
.site-header::after{content:"";position:absolute;left:0;right:0;top:96px;height:1px;background:rgba(255,255,255,.35)}
.brand{position:absolute;left:26px;top:20px;color:#fff}
.brand-name{font-size:34px;font-weight:600;letter-spacing:-1px;line-height:40px}
.brand-tag{font-size:14px;font-weight:600;margin-left:22px}
.social-top{position:absolute;left:278px;top:28px;display:flex;gap:4px}
.social-dot{width:32px;height:32px;border-radius:50%;background:#2f8fc4;border:2px solid #9ad9f6}
.social-dot.active{background:var(--pink);border-color:#f6a9cc}
.search-label{position:absolute;left:842px;top:16px;font-family:"Caveat",cursive;font-size:26px;color:#fff}
.search-arrow{position:absolute;left:788px;top:26px}
.search-box{position:absolute;left:818px;top:52px;width:278px;height:30px;background:#eee;border:1px solid #cfcfcf;border-radius:2px 0 0 2px;font-size:12px;color:#aaa;padding:7px 0 0 30px}
.search-box svg{position:absolute;left:10px;top:8px}
.search-go{position:absolute;left:1096px;top:52px;width:40px;height:30px;background:linear-gradient(#eee,#cfcfcf);border:1px solid #bbb;font-size:14px;color:#444;text-align:center;line-height:28px}

/* sort bar */
.sort-bar{position:absolute;left:0;top:130px;width:1200px;height:65px;background:var(--bar);border-bottom:1px solid #111}
.sort-label{position:absolute;left:14px;top:20px;font-family:"Oswald",sans-serif;font-size:18px;color:#fff;letter-spacing:.5px}
.sort-btn{position:absolute;top:15px;height:35px;background:var(--bar-btn);border:1px solid #222;box-shadow:inset 0 1px 0 #444;color:#fff;font-size:14px;text-align:center;line-height:33px;white-space:nowrap;overflow:hidden}
.sort-btn.current{background:#474747}
.sort-btn.accent{color:var(--pink)}
.sort-more{position:absolute;left:1075px;top:0;width:125px;height:65px;border-left:1px solid #1a1a1a;color:#fff;font-size:15px;line-height:65px;text-align:center}

/* side modules */
.module-nav{position:absolute;left:0;top:195px;width:193px;height:860px;background:var(--side)}
.module{position:absolute;left:0;width:193px;display:flex;align-items:center;justify-content:center;text-align:center;font-size:13px;line-height:13px;color:#eee;text-transform:uppercase;border-bottom:1px solid var(--side-line);box-shadow:inset 0 1px 0 #3a3a3a;padding:0 20px}
.module.plain{text-transform:none;font-size:14px}
.module.hover{background:#474747}
.module.selected{background:#222;color:var(--pink)}
.module.selected::after{content:"";position:absolute;right:0;top:12px;border:7px solid transparent;border-right-color:#fff}

/* books */
.book-card{position:absolute;width:338px;height:222px;background:var(--card);box-shadow:0 2px 4px rgba(0,0,0,.25);padding:4px}
.book-title{height:24px;background:var(--strip);color:#555;font-size:12px;text-align:center;line-height:24px;white-space:nowrap;overflow:hidden}
.book-title small{font-size:10px}
.book-body{display:flex;margin-top:7px}
.book-info{width:192px;padding-left:6px;font-size:12px;line-height:12.5px;color:#777;letter-spacing:-.2px}
.book-info p{margin-top:12.5px}
.book-info p:first-child{margin-top:13px;white-space:nowrap}
.book-info b{font-weight:400;color:#333}
.book-cover{position:relative;width:135px;height:177px;margin-left:auto}
.shop-ribbon{position:absolute;right:-6px;bottom:-8px}
.row-rule{position:absolute;left:240px;width:706px;height:1px;background:#cfcfcf}
.see-more{position:absolute;left:359px;top:990px;width:460px;height:39px;background:#dcdcdc;color:#666;font-size:16px;line-height:39px;text-align:center;letter-spacing:.5px}

/* join banner */
.join-strip{position:absolute;left:980px;top:228px;width:210px;height:4px;background:#cfcfcf}
.join-banner{position:absolute;left:1001px;top:230px}
.join-text{position:absolute;left:1001px;width:164px;text-align:center}
.join-line{top:244px;font-family:"Oswald",sans-serif;font-size:18px;color:#fff}
.join-name{top:294px;font-size:40px;font-weight:600;color:#4db6ea;letter-spacing:-1px}
.join-community{top:344px;font-family:"Oswald",sans-serif;font-size:29px;font-weight:600;color:#1e1e1e}
.join-hint{position:absolute;left:1005px;top:446px;font-family:"Caveat",cursive;font-size:19px;color:#222}
.books-deco{position:absolute;left:985px;top:835px;width:190px;height:110px;border-radius:20px;background:linear-gradient(#e6e6e6,#dadada);opacity:.7}

/* footer */
.site-footer{position:absolute;left:0;top:1055px;width:1200px;height:145px;background:var(--footer)}
.footer-brand{position:absolute;left:52px;top:32px;color:#3c3c3c}
.footer-brand .brand-name{font-size:28px;line-height:32px}
.footer-brand .brand-tag{font-size:12px;margin-left:8px}
.copyright{position:absolute;left:40px;top:109px;font-size:8px;color:#fff}
.footer-col{position:absolute;top:30px}
.footer-col h3{font-size:17px;font-weight:600;color:#fff;margin-bottom:4px}
.footer-col a{display:block;font-size:12.5px;line-height:15px;color:#ddd;text-decoration:none}
.footer-col a.accent{color:var(--pink)}
.social-foot{position:absolute;left:940px;top:57px;display:flex;gap:6px}
.social-foot .social-dot{width:31px;height:31px;background:#111;border-color:#333}
.social-foot .social-dot.active{background:#3aa8e0;border-color:#bfe6fa}
</style>
</head>
<body>

<header class="site-header">
  <div class="brand"><div class="brand-name">Grintax Books</div><div class="brand-tag">powered by Grintax</div></div>
  <div class="social-top"><span class="social-dot active"></span><span class="social-dot"></span><span class="social-dot"></span></div>
  <svg class="search-arrow" width="50" height="46" viewBox="0 0 50 46"><path d="M48 6 C30 -2 4 4 12 40" fill="none" stroke="#fff" stroke-width="2"/><path d="M4 32 L12 42 L20 33" fill="none" stroke="#fff" stroke-width="2"/></svg>
  <div class="search-label">search for your book!</div>
  <div class="search-box"><svg width="12" height="12" viewBox="0 0 12 12"><circle cx="5" cy="5" r="3.6" fill="none" stroke="#aaa" stroke-width="1.5"/><path d="M8 8 L11 11" stroke="#aaa" stroke-width="1.5"/></svg>Search</div>
  <div class="search-go">Go</div>
</header>

<nav class="sort-bar">
  <div class="sort-label">SHORT BY :</div>
  <div class="sort-btn" style="left:112px;width:82px">Show all</div>
  <div class="sort-btn current" style="left:205px;width:83px">Option 2</div>
  <div class="sort-btn accent" style="left:297px;width:85px">Veterinary</div>
  <div class="sort-btn" style="left:391px;width:139px">bigger Option 4</div>
  <div class="sort-btn" style="left:539px;width:84px">Option 5</div>
  <div class="sort-btn" style="left:632px;width:84px">Option 6</div>
  <div class="sort-btn" style="left:725px;width:138px">bigger Option 7</div>
  <div class="sort-btn" style="left:872px;width:137px">bigger Option 8</div>
  <div class="sort-btn" style="left:1018px;width:57px;text-align:left;padding-left:21px">Option 9</div>
  <div class="sort-more">&#8810;&nbsp;&nbsp;more&nbsp;&nbsp;&#8811;</div>
</nav>

<aside class="module-nav">
  <div class="module plain" style="top:0;height:56px">All modules</div>
  <div class="module" style="top:56px;height:50px">Electrochemistry<br>(C option)</div>
  <div class="module" style="top:106px;height:62px">Organic chemistry for the biological sciences</div>
  <div class="module" style="top:168px;height:50px">Nucleic acid and peptide chemistry</div>
  <div class="module" style="top:218px;height:50px">Basic biology for nanotechnology</div>
  <div class="module" style="top:268px;height:52px">Medicinal chemistry of anti-infectives</div>
  <div class="module hover" style="top:320px;height:60px">Heterocyclic chemistry and drug synthesis</div>
  <div class="module" style="top:380px;height:50px">Surface science<br>(C option)</div>
  <div class="module selected" style="top:430px;height:38px">Spectroscopy</div>
  <div class="module" style="top:468px;height:50px">Spectroscopy<br>(distance learning)</div>
  <div class="module" style="top:518px;height:50px">Higher organic chemistry</div>
  <div class="module" style="top:568px;height:62px">Modern applications of physical chemistry(BSc)</div>
  <div class="module" style="top:630px;height:50px">Further physical chemistry (MChem)</div>
  <div class="module" style="top:680px;height:38px">Catalysis</div>
  <div class="module" style="top:718px;height:50px">Catalysis (distance learning)</div>
  <div class="module" style="top:768px;height:40px">Organic chemistry II</div>
  <div class="module plain" style="top:808px;height:52px;border-bottom:0">See more</div>
</aside>

<main>
  <article class="book-card" style="left:240px;top:229px">
    <div class="book-title">Spin and structure | <small>A primer in practical resonance methods</small></div>
    <div class="book-body">
      <div class="book-info"><p><b>University:</b> University of Calbury</p><p><b>Faculty:</b> Chemistry</p><p><b>Course:</b> SPECTROSCOPY</p><p><b>Authors:</b> H. L. Verrow and<br>C. T. Dask</p><p><b>Year:</b> 2003</p><p><b>Publisher:</b> Harbrook Thornby</p></div>
      <div class="book-cover" role="img" aria-label="Book cover artwork" style="background:linear-gradient(#4a4d6a,#2c2f45)">
        <svg class="shop-ribbon" width="56" height="56" viewBox="0 0 56 56"><polygon points="56,0 56,22 22,56 0,56" fill="#fff"/></svg>
      </div>
    </div>
  </article>
  <article class="book-card" style="left:609px;top:229px">
    <div class="book-title">Principles of Molecular Light Analysis</div>
    <div class="book-body">
      <div class="book-info"><p><b>University:</b> University of Calbury</p><p><b>Faculty:</b> Chemistry</p><p><b>Course:</b> SPECTROSCOPY</p><p><b>Authors:</b> Tollerby</p><p><b>Year:</b> 1997</p><p><b>Publisher:</b> Castell-Marsh</p></div>
      <div class="book-cover" role="img" aria-label="Book cover artwork" style="background:linear-gradient(135deg,#b5542a,#d9c9a5)">
        <svg class="shop-ribbon" width="56" height="56" viewBox="0 0 56 56"><polygon points="56,0 56,22 22,56 0,56" fill="#fff"/></svg>
      </div>
    </div>
  </article>
  <div class="row-rule" style="top:468px"></div>

  <article class="book-card" style="left:240px;top:489px">
    <div class="book-title">Interfaces</div>
    <div class="book-body">
      <div class="book-info"><p><b>University:</b> University of Calbury</p><p><b>Faculty:</b> Chemistry</p><p><b>Course:</b> SPECTROSCOPY</p><p><b>Authors:</b> Marek Orlin, Simon<br>Faddle</p><p><b>Year:</b> 1999</p><p><b>Publisher:</b> Elmford Chemistry<br>Primers</p></div>
      <div class="book-cover" role="img" aria-label="Book cover artwork" style="background:linear-gradient(#8a3a8e,#5b2a7a)">
        <svg class="shop-ribbon" width="56" height="56" viewBox="0 0 56 56"><polygon points="56,0 56,22 22,56 0,56" fill="#fff"/></svg>
      </div>
    </div>
  </article>
  <article class="book-card" style="left:609px;top:489px">
    <div class="book-title">Spin and structure | <small>A primer in practical resonance methods</small></div>
    <div class="book-body">
      <div class="book-info"><p><b>University:</b> University of Calbury</p><p><b>Faculty:</b> Chemistry</p><p><b>Course:</b> SPECTROSCOPY</p><p><b>Authors:</b> R. J. Kestwood and<br>P. N. Averil</p><p><b>Year:</b> 2005</p><p style="white-space:nowrap;letter-spacing:-.4px"><b>Publisher:</b> Elmford University Press</p></div>
      <div class="book-cover" role="img" aria-label="Book cover artwork" style="background:linear-gradient(#4b4a9a,#3a3a7e)">
        <svg class="shop-ribbon" width="56" height="56" viewBox="0 0 56 56"><polygon points="56,0 56,22 22,56 0,56" fill="#fff"/></svg>
      </div>
    </div>
  </article>
  <div class="row-rule" style="top:728px"></div>

  <article class="book-card" style="left:240px;top:746px">
    <div class="book-title">Magnetic resonance methods in chemistry</div>
    <div class="book-body">
      <div class="book-info"><p><b>University:</b> University of Calbury</p><p><b>Faculty:</b> Chemistry</p><p><b>Course:</b> SPECTROSCOPY</p><p><b>Authors:</b> L. M. Quennel</p><p><b>Year:</b> 1989</p><p><b>Publisher:</b> Draycott</p></div>
      <div class="book-cover" role="img" aria-label="Book cover artwork" style="background:linear-gradient(#5a3418,#a8652e)">
        <svg class="shop-ribbon" width="56" height="56" viewBox="0 0 56 56"><polygon points="56,0 56,22 22,56 0,56" fill="#fff"/></svg>
      </div>
    </div>
  </article>
  <article class="book-card" style="left:609px;top:746px">
    <div class="book-title">Resonance in crystalline solids</div>
    <div class="book-body">
      <div class="book-info"><p><b>University:</b> University of Calbury</p><p><b>Faculty:</b> Chemistry</p><p><b>Course:</b> SPECTROSCOPY</p><p><b>Authors:</b> A. F. Pellow</p><p><b>Year:</b> 2007</p><p><b>Publisher:</b> Whitmere Publisher</p></div>
      <div class="book-cover" role="img" aria-label="Book cover artwork" style="background:linear-gradient(135deg,#0e0e0e,#3c3c3c)">
        <svg class="shop-ribbon" width="56" height="56" viewBox="0 0 56 56"><polygon points="56,0 56,22 22,56 0,56" fill="#fff"/></svg>
      </div>
    </div>
  </article>

  <div class="see-more">SEE MORE</div>
</main>

<aside>
  <div class="join-strip"></div>
  <svg class="join-banner" width="164" height="198" viewBox="0 0 164 198">
    <polygon points="0,0 164,0 164,196 82,168 0,196" fill="var(--banner-edge)"/>
    <polygon points="6,4 158,4 158,186 82,160 6,186" fill="var(--banner)"/>
    <line x1="20" y1="42" x2="72" y2="42" stroke="#888"/><line x1="92" y1="42" x2="144" y2="42" stroke="#888"/>
    <polygon points="82,36 84,41 89,41 85,44 86,49 82,46 78,49 79,44 75,41 80,41" fill="#777"/>
  </svg>
  <div class="join-text join-line">CLICK TO JOIN THE</div>
  <div class="join-text join-name">Grintax</div>
  <div class="join-text join-community">COMMUNITY</div>
  <svg class="abs" style="left:1138px;top:425px" width="26" height="40" viewBox="0 0 26 40"><path d="M4 38 C22 30 20 12 8 4" fill="none" stroke="#222" stroke-width="1.5"/><path d="M4 12 L7 3 L15 6" fill="none" stroke="#222" stroke-width="1.5"/></svg>
  <div class="join-hint">This way to the progress!</div>
  <div class="books-deco" role="img" aria-label="Faint sketch of a stack of books"></div>
</aside>

<footer class="site-footer">
  <div class="footer-brand"><div class="brand-name">Grintax Books</div><div class="brand-tag">powered by Grintax</div></div>
  <div class="copyright">COPYRIGHT 2012 ALL RIGHTS RESERVED</div>
  <div class="footer-col" style="left:407px"><h3>Info</h3><a>About</a><a>FAQS</a><a class="accent">Contact us</a><a>Blog</a></div>
  <div class="footer-col" style="left:527px"><h3>Social</h3><a>Palvio</a><a>Chirrup</a><a>Tandrell</a></div>
  <div class="footer-col" style="left:649px"><h3>Legal</h3><a>Terms &amp; Conditions</a><a>Privacy Policy</a></div>
  <div class="social-foot"><span class="social-dot active"></span><span class="social-dot"></span><span class="social-dot"></span></div>
</footer>

</body>
</html>
```